Brochure Design Project

We are a consulting engineering company and need to have our current company brochure updated and made to look a lot more professional.

We provide design and documentation of electrical, lighting, mechanical, hydraulic, fire, services to architects, interior designers, building owners and managers.

We are launching an updated website shortly and want a print brochure to send to clients.

Attached is our current brochure for reference.
Updates

The recent projects section should be renamed to "Completed Projects". Space should be allowed for 8 projects. I have uploaded 7 of these images and a new image will follow shortly.

We would like to include an image for each of our company services. I have uploaded 9 new images:

1. Electrical
2. Mechanical
3. Communications
4. Fire
5. Security
6. Lighting
7. Hydraulics
8. Computer Suite
9. Building Assessments

Target Market(s)

Architects, Interior Designers, Consultants, Professionals

Industry/Entity Type

Building

Requirements
Must have
• Very professional look
Simple and easy to read layout
Similar look and feel to our new website which is soon to be launched : http://www.loomtrail.co.uk/hvk/
Examples of our recent projects - around 6 projects with 1 or 2 photos per project. Will upload these soon.
A3 size, double sided with centre fold
Should not have
• Bright colours
Any comics or similar

```html
<!DOCTYPE html>
<html lang="en">
<head>
<meta charset="utf-8">
<title>Services Brochure Spread</title>
<link rel="stylesheet" href="https://fonts.googleapis.com/css2?family=PT+Sans:wght@400;700&display=swap">
<style>
  :root {
    --page-bg: #ffffff;
    --canvas-bg: #f4f4f4;
    --band-mid: #a6a6a8;
    --band-edge: #d6d6d8;
    --heading: #2b2b2b;
    --body: #3a3a3a;
    --dark: #262626;
    --frame: #ffffff;
    --fold: #b8b8b8;
  }
  * { margin: 0; padding: 0; box-sizing: border-box; }
  html, body { width: 1200px; height: 867px; overflow: hidden; background: var(--canvas-bg); }
  body { position: relative; font-family: "PT Sans", Arial, sans-serif; color: var(--body); }

  .spread {
    position: absolute; left: 28px; top: 28px; width: 1143px; height: 810px;
    background: var(--page-bg); box-shadow: 0 2px 6px rgba(0,0,0,.35); overflow: hidden;
  }
  .title-band {
    position: absolute; left: 0; top: 0; width: 100%; height: 94px;
    background: linear-gradient(to right, var(--band-edge) 0%, var(--band-mid) 4%, var(--band-mid) 96%, var(--band-edge) 100%);
    border-bottom: 4px solid #c9c9cb;
  }
  .title-band h1 {
    position: absolute; left: 59px; top: 59px; font-size: 15px; font-weight: 700; color: var(--heading);
  }
  .fold-line {
    position: absolute; left: 571px; top: 0; height: 385px; border-left: 1px dashed var(--fold);
  }

  .service { position: absolute; width: 225px; }
  .service h2 {
    font-size: 12px; font-weight: 700; color: var(--heading); line-height: 15px; margin-bottom: 1px;
  }
  .service li {
    list-style: none; font-size: 8.6px; line-height: 9.6px; padding-bottom: 1.7px; color: var(--body);
  }

  .projects {
    position: absolute; left: 0; top: 385px; width: 100%; height: 425px; background: var(--dark);
  }
  .projects h2 {
    position: absolute; left: 59px; top: 17px; font-size: 15px; font-weight: 700; color: #fff;
  }
  .project-photo { position: absolute; border: 4px solid var(--frame); }
</style>
</head>
<body>
<div class="spread">
  <div class="title-band"><h1>Services</h1></div>
  <div class="fold-line"></div>

  <section class="service" style="left:59px; top:111px;">
    <h2>Electrical Services</h2>
    <ul>
      <li>Power distribution</li>
      <li>General lighting</li>
      <li>Feature lighting for highlight/contrast of client orientated areas</li>
      <li>Programmable lighting control</li>
      <li>Emergency lighting and exit signs</li>
      <li>Electrical consumption management</li>
      <li>Lighting control integration with energy management systems</li>
      <li>Evacuation warning systems</li>
      <li>Power conditioners</li>
      <li>Public address installations</li>
      <li>Television signal distribution</li>
    </ul>
  </section>
  <section class="service" style="left:59px; top:281px;">
    <h2>Computer Suite Audits</h2>
    <ul>
      <li>Comprehensive Computer Suite Audits</li>
      <li>Australian Standard Compliance</li>
      <li>TIA 942 Tier Rating certification</li>
    </ul>
  </section>

  <section class="service" style="left:315px; top:111px;">
    <h2>Critical Use Installations</h2>
    <ul>
      <li>Layout and space allowance for hardware and equipment</li>
      <li>Uninterruptable power supplies and power conditioning</li>
      <li>Access control and intruder detection</li>
      <li>Fire rating</li>
      <li>Anti static solutions</li>
      <li>PABX and VOIP integration</li>
      <li>Dedicated electrical distribution systems</li>
      <li>Stand-by power supplies</li>
      <li>High heat rejection cooling solutions</li>
    </ul>
  </section>
  <section class="service" style="left:315px; top:238px;">
    <h2>Hydraulic Services</h2>
    <ul>
      <li>Water supplies</li>
      <li>Waste discharge</li>
      <li>Venting</li>
      <li>Water heating and cooling</li>
      <li>Filtration</li>
    </ul>
  </section>

  <section class="service" style="left:632px; top:111px; width:245px;">
    <h2>Communication Systems</h2>
    <ul>
      <li>Telephone cabling</li>
      <li>Data cabling</li>
      <li>Patching philosophies</li>
      <li>Fibre optic distribution systems</li>
      <li>Integration of voice and</li>
      <li>data cabling systems</li>
      <li>Hardware housings</li>
      <li>Compliance with relevant codes and installation practices</li>
      <li>LAN Cable distribution systems</li>
    </ul>
  </section>
  <section class="service" style="left:632px; top:238px; width:245px;">
    <h2>Mechanical Services</h2>
    <ul>
      <li>District Cooling System</li>
      <li>Air and Water Cooled Chilled Water System</li>
      <li>BMS/BAS and DDC Control System</li>
      <li>Computer and Data Centre Solutions</li>
      <li>DX-Type Water and Air</li>
      <li>Cooled System (Single or</li>
      <li>Multiple Indoor Units)</li>
      <li>VAV and Chilled Beams</li>
      <li>Industrial and Commercial</li>
      <li>Humidification</li>
      <li>Commercial and Industrial Evaporative Cooling Using Air Washers</li>
    </ul>
  </section>

  <section class="service" style="left:887px; top:111px; width:215px;">
    <h2>Security Services</h2>
    <ul>
      <li>Electronic access control</li>
      <li>Integration of existing systems with client requirements</li>
      <li>Intruder detection</li>
      <li>Off site monitoring and alarms</li>
      <li>CCTV</li>
    </ul>
  </section>
  <section class="service" style="left:887px; top:193px; width:215px;">
    <h2>Fire Services</h2>
    <ul>
      <li>Electronic Smoke and Thermal Detection</li>
      <li>VENTRA Systems</li>
      <li>Fire Suppression Systems</li>
      <li>Fire Sprinkler Systems</li>
    </ul>
  </section>
  <section class="service" style="left:887px; top:264px; width:215px;">
    <h2>Building Assessment</h2>
    <ul>
      <li>Building services condition assessment</li>
      <li>Advise relative to available building services (for long or short term purpose)</li>
      <li>Trouble Shooting and Investigation</li>
      <li>Review of Existing Systems</li>
      <li>Upgrade for Current and Future Refurbishment</li>
    </ul>
  </section>

  <section class="projects">
    <h2>Recent Projects</h2>
    <div class="project-photo" role="img" aria-label="Boardroom with long table, black chairs and brick wall" style="left:59px; top:47px; width:230px; height:154px; background:linear-gradient(135deg,#e8e6e2,#b9ada0 60%,#6b5a4e);"></div>
    <div class="project-photo" role="img" aria-label="Meeting room with projection screen and orange accents" style="left:304px; top:47px; width:230px; height:154px; background:linear-gradient(160deg,#e4e4e4,#a8a8a8 55%,#3e3e42);"></div>
    <div class="project-photo" role="img" aria-label="Large empty warehouse hall with high bay lights" style="left:596px; top:47px; width:230px; height:154px; background:linear-gradient(180deg,#4a4338,#8a7f6c 50%,#c2bcae);"></div>
    <div class="project-photo" role="img" aria-label="Blue glass office tower against the sky" style="left:846px; top:47px; width:120px; height:154px; background:linear-gradient(180deg,#9ec3e6,#2e5d9e 60%,#1c335e);"></div>
    <div class="project-photo" role="img" aria-label="Glass high-rise beside heritage street buildings" style="left:970px; top:47px; width:117px; height:154px; background:linear-gradient(180deg,#8fb3d9,#a9b6c1 50%,#8a7a66);"></div>
    <div class="project-photo" role="img" aria-label="Booth seating with lime green upholstery" style="left:59px; top:217px; width:230px; height:154px; background:linear-gradient(90deg,#d9c9a8,#9aa83a 35%,#3a3a3a 70%,#a6b63e);"></div>
    <div class="project-photo" role="img" aria-label="Open plan office with white desks" style="left:304px; top:217px; width:230px; height:154px; background:linear-gradient(160deg,#f0f0f0,#c8c8c8 60%,#5a5a5e);"></div>
    <div class="project-photo" role="img" aria-label="Two-storey heritage building lit at dusk" style="left:596px; top:217px; width:230px; height:154px; background:linear-gradient(180deg,#27406e,#8a6a3c 55%,#d9a24a 75%,#3c5a2a);"></div>
    <div class="project-photo" role="img" aria-label="Office reception with timber floor and feature stair" style="left:851px; top:217px; width:230px; height:154px; background:linear-gradient(180deg,#2a2a2a,#8c8c8c 45%,#d8d4cc);"></div>
  </section>
</div>
</body>
</html>
```